Design and put together a 5 page A4 brochure for a Training Programme

Carrowmere Institute of Training deliver a Nationally Accredited Programme in Medical Reception and Administration.

We have a new Qualification (Cert III Business Administration) and we require a 5 page brochure to be designed. (I have CHANGED THIS TO 5 Pages as I can see it is too crowded and not clean enough)

I would put a 6th page in as an application form.

We have recently rebranded our website which is currently under development - so a .jpg will be available of the 'look and feel of this'. I will also upload some stock photos which could be used in the design.

This is an important project for us - so your fantastic work will be greatly appreciated.

This project is fairly urgent - so it is likely we will be choosing a 'winner' to work with sooner rather than later.

Thanks for considering!

I will be uploading various graphics/drafts now.
Updates

Target Market(s)

1/ Women 25-45 yrs undertaking studies in being a medical receptionist
2/ Medical Practices who are hiring Trainees for their medical clinic or hospital

Industry/Entity Type

Medical

Font styles to use
Serif
Sans Serif

Colors
0455a3
fbe7d2
f68e4e
fef4ee
3176b5
33a6d7
f37122

Requirements
Must have
• Clear and clean design - professional
• Graphics of medical pictures (I will supply some so you get the look and feel of wht we are looking for)
• Corporate branding (I will upload a .jpg of new website design for look and feel
• The colour I would like with blue is also a STONE colour - I could not find it in the colour wheel on this site.
• The partner logos should be on the last page probably in one faded colour (such as grey)
Should not have
• I must be able to see the inside of the brochure also, I can not pick this purely on the front cover. Thanks :-)
• I have also now updated the Company Logo

```html
<!DOCTYPE html>
<html lang="en">
<head>
<meta charset="utf-8">
<title>Carrowmere Institute of Training – Medical Administration Brochure Spread</title>
<link rel="stylesheet" href="https://fonts.googleapis.com/css2?family=Didact+Gothic&family=Poppins:wght@500;600;700&display=swap">
<style>
  :root {
    --navy: #2c3e5c;
    --tab: #2f3e5a;
    --orange: #e2662a;
    --orange-band: #e8772e;
    --sky: #1fa3d8;
    --royal: #0a5a9e;
    --pale-blue: #9dcbe1;
    --stone: #f3e8df;
    --rule: #e3e6ea;
    --paper: #ffffff;
    --bg: #e9eef2;
  }
  * { margin: 0; padding: 0; box-sizing: border-box; }
  html, body { width: 1200px; height: 1200px; overflow: hidden; background: var(--bg); }
  body { position: relative; font-family: "Didact Gothic", sans-serif; color: var(--navy); }

  .spread {
    position: absolute; left: 20px; top: 192px;
    width: 1240px; height: 873px;
    transform: scale(0.9355); transform-origin: 0 0;
    box-shadow: 0 18px 30px rgba(0,0,0,.25);
  }
  .page { position: absolute; top: 0; height: 873px; width: 620px; background: var(--paper); overflow: hidden; }
  .page--left { left: 0; background: linear-gradient(90deg, #fff 80%, #eef0f2 100%); }
  .page--right { left: 620px; }

  .abs { position: absolute; }

  /* Left page */
  .course-title { left: 35px; top: 22px; font-family: "Poppins", sans-serif; font-weight: 600; font-size: 30px; }
  .course-sub { left: 35px; top: 57px; color: var(--orange); font-size: 16px; line-height: 18.5px; width: 200px; }
  .photo-stethoscope { left: 390px; top: 15px; width: 185px; height: 140px; border-radius: 50%;
    background: radial-gradient(circle at 50% 55%, #3fb4b0 0%, #8fcfcc 45%, #fff 72%); }

  .unit-group { left: 30px; width: 508px; }
  .unit-tab { display: inline-block; background: var(--tab); color: #fff; font-family: "Poppins", sans-serif; font-weight: 600;
    font-size: 14px; line-height: 17px; padding: 3px 9px; }
  .unit-row { display: flex; border-bottom: 1px solid var(--rule); border-left: 1px solid var(--rule); border-right: 1px solid var(--rule);
    font-size: 13px; min-height: 25px; align-items: center; }
  .unit-row .code { width: 133px; padding-left: 15px; flex: none; }
  .unit-row .desc { line-height: 15px; padding: 2px 0; }

  .bonus-band { left: 0; top: 605px; width: 620px; height: 101px; background: var(--orange-band); padding: 7px 28px 0 30px; }
  .bonus-band h3 { text-align: center; font-family: "Poppins", sans-serif; font-weight: 600; font-size: 14px; color: #2a2a2a; margin-bottom: 4px; }
  .bonus-band p { font-size: 12.5px; line-height: 15px; text-align: justify; color: var(--tab); }

  .career-box { left: 30px; top: 718px; width: 281px; height: 155px; background: var(--sky); color: #fff; padding: 12px 6px 0 5px; }
  .career-box h2 { font-family: "Poppins", sans-serif; font-weight: 600; font-size: 30px; line-height: 34px; margin-bottom: 8px; }
  .career-box p { font-size: 14px; line-height: 16px; }
  .career-list { left: 340px; top: 715px; list-style: none; font-size: 13px; line-height: 14.6px; }
  .career-list li::before { content: ""; display: inline-block; border-left: 6px solid var(--sky); border-top: 4px solid transparent;
    border-bottom: 4px solid transparent; margin-right: 8px; }
  .career-edge { left: 591px; top: 718px; width: 29px; height: 155px; background: var(--sky); }

  /* Right page */
  .openings { left: 18px; top: 0; width: 282px; height: 151px; background: var(--orange); color: #fff; padding: 24px 10px 0 10px;
    font-family: "Poppins", sans-serif; font-weight: 600; font-size: 21.5px; line-height: 27.5px; }
  .openings .sub { margin-top: 7px; display: block; }
  .graphics { left: 0; top: 0; }
  .insights-title { left: 412px; top: 48px; font-family: "Poppins", sans-serif; font-weight: 600; font-size: 13.5px; color: #1c1c1c; }
  .hex-label { position: absolute; font-family: "Poppins", sans-serif; font-weight: 500; font-size: 8.5px; line-height: 10px; text-align: center; color: #222; width: 100px; }
  .chart-note { left: 25px; top: 336px; width: 360px; font-size: 9.5px; line-height: 11px; text-align: center; color: #333; }
  .chart-note small { display: block; font-size: 7px; line-height: 8px; }

  .package-title { left: 28px; top: 383px; font-family: "Poppins", sans-serif; font-weight: 600; font-size: 23px; }
  .package-intro { left: 28px; top: 426px; width: 560px; font-size: 13px; line-height: 15px; }
  .package-list { left: 28px; top: 467px; width: 540px; list-style: none; font-size: 13px; line-height: 15.8px; }
  .package-list li { padding-left: 11px; text-indent: -11px; }
  .package-list li::before { content: "• "; }
  .photo-bag { left: 460px; top: 578px; width: 90px; height: 114px; background: linear-gradient(160deg, #ee3a3a, #c91414); border-radius: 4px 4px 8px 8px; }

  .entry-title { left: 28px; top: 740px; font-family: "Poppins", sans-serif; font-weight: 600; font-size: 26px; }
  .entry-text { left: 30px; top: 784px; width: 563px; font-size: 12.5px; line-height: 15px; text-align: justify; }
</style>
</head>
<body>
<div class="spread">

  <section class="page page--left">
    <h1 class="abs course-title">Course</h1>
    <p class="abs course-sub">Units of Competency Covered in the Carrowmere Programme</p>
    <div class="abs photo-stethoscope" role="img" aria-label="Stethoscope photograph"></div>

    <div class="abs unit-group" style="top:141px">
      <span class="unit-tab">Core</span>
      <div class="unit-row"><span class="code">BSBITU307</span><span class="desc">Develop keyboarding speed and accuracy</span></div>
      <div class="unit-row"><span class="code">BSBWHS201</span><span class="desc">Contribute to health and safety of self and others</span></div>
    </div>

    <div class="abs unit-group" style="top:222px">
      <span class="unit-tab">Medical Skill Set</span>
      <div class="unit-row"><span class="code">BSBMED301</span><span class="desc">Interpret and apply medical terminology appropriately</span></div>
      <div class="unit-row"><span class="code">BSBMED302</span><span class="desc">Prepare and process medical accounts</span></div>
      <div class="unit-row"><span class="code">BSBMED303</span><span class="desc">Maintain patient records</span></div>
      <div class="unit-row" style="min-height:33px"><span class="code">BSBMED305</span><span class="desc">Apply the principles of confidentiality, privacy<br>and security within the medical environment</span></div>
      <div class="unit-row"><span class="code">BSBMED304</span><span class="desc">Assist in controlling stocks and supplies</span></div>
    </div>

    <div class="abs unit-group" style="top:384px">
      <span class="unit-tab">Business Administration (Medical) Skill Set including<br>an introduction to Audio-typing</span>
      <div class="unit-row"><span class="code">BSBITU309</span><span class="desc">Produce desktop published documents</span></div>
      <div class="unit-row"><span class="code">BSBITU303</span><span class="desc">Design and produce text documents</span></div>
      <div class="unit-row"><span class="code">BSBITU306</span><span class="desc">Design and produce business documents</span></div>
      <div class="unit-row"><span class="code">BSBWRT301</span><span class="desc">Write simple documents</span></div>
      <div class="unit-row"><span class="code">BSBADM303</span><span class="desc">Produce texts from audio transcription</span></div>
    </div>

    <div class="abs unit-group" style="top:550px">
      <span class="unit-tab">Customer Service for Medical Administrators</span>
      <div class="unit-row"><span class="code">BSBCUS301</span><span class="desc">Deliver and monitor a service to customers</span></div>
    </div>

    <div class="abs bonus-band">
      <h3>Bonus training offered as part of the Carrowmere Programme</h3>
      <p>• Medical Triage for Non-Clinical Staff and Customer Service (BSBCUS301 • CPR First Aid Qualification with National First Aid Society (BSBSXXXXX) • DocuWrite 2010 Essentials Short Course • PageCraft 2010 Essentials Short Course • Carrowmere Typefast Online Keyboard Programme and certification to Australian Standards</p>
    </div>

    <div class="abs career-box">
      <h2>Career Outcomes</h2>
      <p>Completing your Certificate III in Business Administration (Medical), you’ll be qualified to work in the following areas</p>
    </div>
    <ul class="abs career-list">
      <li>Medical Receptionist</li>
      <li>Medical Secretary</li>
      <li>Administration Assistant</li>
      <li>Medical Administration</li>
      <li>Ward Clerk</li>
      <li>Dental Receptionist</li>
      <li>Medical Accounts Clerk</li>
      <li>Medical Records Administration</li>
      <li>Front Desk Hospital Admissions</li>
    </ul>
    <div class="abs career-edge"></div>
  </section>

  <section class="page page--right">
    <div class="abs openings">MEDICAL<br>RECEPTIONIST<br>(ANZSCO CODE 542114)<span class="sub">Expected job Openings</span></div>

    <svg class="abs graphics" width="620" height="380" viewBox="620 0 620 380" aria-hidden="true">
      <g fill="var(--pale-blue)" stroke="#fff" stroke-width="7" stroke-linejoin="round">
        <path d="M825,338 L653,338 A172,172 0 0 1 686,237 Z"/>
        <path d="M825,338 L686,237 A172,172 0 0 1 772,174 Z"/>
        <path d="M825,338 L772,174 A172,172 0 0 1 878,174 Z"/>
        <path d="M825,338 L878,174 A172,172 0 0 1 964,237 Z"/>
        <path d="M825,338 L964,237 A172,172 0 0 1 997,338 Z" fill="var(--royal)"/>
      </g>
      <g font-family="Poppins, sans-serif" font-weight="500" font-size="13" fill="#fff">
        <text x="693" y="310">LOW</text>
        <text x="790" y="200">AVERAGE</text>
        <text x="916" y="310">HIGH</text>
      </g>

      <g fill="var(--stone)">
        <polygon points="0,-1 0.866,-0.5 0.866,0.5 0,1 -0.866,0.5 -0.866,-0.5" transform="translate(1032,148) scale(74)"/>
        <polygon points="0,-1 0.866,-0.5 0.866,0.5 0,1 -0.866,0.5 -0.866,-0.5" transform="translate(1163,148) scale(74)"/>
        <polygon points="0,-1 0.866,-0.5 0.866,0.5 0,1 -0.866,0.5 -0.866,-0.5" transform="translate(1098,255) scale(74)"/>
      </g>
      <polygon fill="var(--royal)" points="0,-1 0.866,-0.5 0.866,0.5 0,1 -0.866,0.5 -0.866,-0.5" transform="translate(1000,25) scale(14)"/>
      <polygon fill="var(--sky)" points="0,-1 0.866,-0.5 0.866,0.5 0,1 -0.866,0.5 -0.866,-0.5" transform="translate(973,63) scale(29)"/>
      <polygon fill="var(--royal)" points="0,-1 0.866,-0.5 0.866,0.5 0,1 -0.866,0.5 -0.866,-0.5" transform="translate(1204,27) scale(29)"/>
      <polygon fill="#ea8a3c" points="0,-1 0.866,-0.5 0.866,0.5 0,1 -0.866,0.5 -0.866,-0.5" transform="translate(1015,240) scale(14)"/>
      <polygon fill="#ea8a3c" points="0,-1 0.866,-0.5 0.866,0.5 0,1 -0.866,0.5 -0.866,-0.5" transform="translate(1197,243) scale(30)"/>
      <polygon fill="var(--sky)" points="0,-1 0.866,-0.5 0.866,0.5 0,1 -0.866,0.5 -0.866,-0.5" transform="translate(1226,313) scale(16)"/>

      <!-- growth bar -->
      <rect x="1020" y="132" width="25" height="43" fill="#9a9a9a"/>
      <polygon points="1017,132 1032,117 1048,132" fill="#20b3ad"/>
      <rect x="1020" y="124" width="25" height="9" fill="#20b3ad"/>
      <!-- jobs by location bars -->
      <g fill="#20b3ad">
        <rect x="1126" y="109" width="7" height="63"/>
        <rect x="1135" y="132" width="7" height="40"/>
        <rect x="1144" y="134" width="7" height="38"/>
        <rect x="1153" y="160" width="7" height="12"/>
        <rect x="1162" y="162" width="7" height="10"/>
        <rect x="1171" y="168" width="7" height="4"/>
        <rect x="1180" y="170" width="7" height="2"/>
        <rect x="1189" y="170" width="9" height="2"/>
      </g>
      <!-- openings icon -->
      <rect x="1072" y="252" width="12" height="30" fill="#9a9a9a"/>
      <rect x="1086" y="247" width="30" height="30" rx="6" fill="#9a9a9a"/>
      <rect x="1096" y="227" width="22" height="20" rx="3" fill="#20b3ad"/>
      <circle cx="1107" cy="237" r="5" fill="#fff"/>
    </svg>

    <h2 class="abs insights-title">INDUSTRY INSIGHTS</h2>
    <div class="hex-label" style="left:362px;top:183px">Growth in the past<br>5 years</div>
    <div class="hex-label" style="left:493px;top:180px">Jobs by location</div>
    <div class="hex-label" style="left:428px;top:289px">Median full time<br>weekly Openings</div>

    <p class="abs chart-note">162,200 persons were employed as Receptionists in 2014, job opening over the next 5 years are expected to be greater then 50,000
      <small>Source : Bureau of Workforce Statistics for full details on Receptionists visit job Outlook</small>
      <small>Source : www.careerforecast.example</small></p>

    <h2 class="abs package-title">The student study package – what you receive</h2>
    <p class="abs package-intro">Students receive an array of helpful resources to keep as part of the Carrowmere Programme. These include</p>
    <ul class="abs package-list">
      <li>Carrowmere Institute Workbook ‘Medical Receptionist and Secretary’s Handbook’</li>
      <li>Carrowmere Institute Workbook ‘Write, Design and Produce Documents for the Australian Medical Office’</li>
      <li>Carrowmere Institute Workbook ‘Medical Triage and Customer Service for non-clinical staff’</li>
      <li>Access to Carrowmere Online Learning platform</li>
      <li>Access to Carrowmere Type-fast programme with testing and certification to Australian standards</li>
      <li>DocuWrite and PageCraft online tutorials and certification</li>
      <li>Digital Medical Transcription Software – student version.</li>
      <li>Medical Accounts Software ClinicLedger – demo version to keep</li>
      <li>CPP endorsed Triage Guide Chart</li>
      <li>First Aid Society Basic First Aid Booklet and CPR Wallet Card</li>
      <li>CPR Accredited Training</li>
      <li>Cardiac Care Alliance endorsed online training programme</li>
      <li>Cardiac Care Alliance DVD and Facts Pack for medical professionals</li>
      <li>Access to accredited specialist mentors and trainers</li>
      <li>Registration into Carrowmere’s Job-Network Club</li>
    </ul>
    <div class="abs photo-bag" role="img" aria-label="Red tote bag photograph"></div>

    <h2 class="abs entry-title">Entry Requirements</h2>
    <p class="abs entry-text">There are no formal entry requirements for this qualification, however it is recommended that individuals have a Year 10 standard of English and basic keyboard skills. Students with English as a second language may request a language, literacy and numeracy assessment during the enrolment and orientation session to determine learning support needs.</p>
  </section>

</div>
</body>
</html>
```